Electrical company needs professional eye catching business cards

I am an electrician who needs business cards. I have attached two images which you can use. The file ab.jpg I would atleast like to be used. The file named back.jpg can be used on the back or not... up to you.

The information on my business cards I will have displayed will be-
My name
Mobile number
web site url
Licence number
ABN

Also as another request, I would like the word "Electrician" on the front of the card somewhere. Maybe under my name or something?

Industry/Entity Type

Electrician

```html
<!DOCTYPE html>
<html lang="en">
<head>
<meta charset="utf-8">
<title>Norvale Installations – Business Cards</title>
<link rel="stylesheet" href="https://fonts.googleapis.com/css2?family=Source+Sans+3:wght@400;600;700&display=swap">
<style>
  :root {
    --backdrop: #e9e8e6;
    --card-white: #f7f7f5;
    --card-black: #262626;
    --brand-blue: #2b3590;
    --ink: #2a2a2a;
    --ink-soft: #6b6b6b;
    --watermark: #ececea;
  }
  * { margin: 0; padding: 0; box-sizing: border-box; }
  html, body {
    width: 1200px;
    height: 900px;
    overflow: hidden;
    background: var(--backdrop);
    font-family: "Source Sans 3", "Myriad Pro", Arial, sans-serif;
  }
  .sheet {
    position: relative;
    width: 1200px;
    height: 900px;
  }
  .card {
    position: absolute;
    left: 320px;
    width: 560px;
    height: 320px;
    overflow: hidden;
    box-shadow: 0 6px 18px rgba(0,0,0,0.14);
  }

  /* Back of card */
  .card--back {
    top: 100px;
    background: var(--card-black);
    display: flex;
    align-items: center;
    justify-content: center;
  }
  .card--back .back-name {
    color: var(--brand-blue);
    font-weight: 700;
    font-size: 64px;
    letter-spacing: 1px;
  }

  /* Front of card */
  .card--front {
    top: 480px;
    background: var(--card-white);
    color: var(--ink);
  }
  .watermark {
    position: absolute;
    right: -10px;
    top: 18px;
    font-weight: 700;
    font-size: 150px;
    line-height: 1;
    color: var(--watermark);
    letter-spacing: -2px;
  }
  .registration {
    position: absolute;
    top: 30px;
    right: 36px;
    text-align: right;
    font-size: 13px;
    line-height: 1.45;
    color: var(--ink-soft);
  }
  .brand {
    position: absolute;
    left: 40px;
    top: 104px;
    display: flex;
    align-items: center;
    gap: 12px;
  }
  .brand-square {
    width: 44px;
    height: 44px;
    background: var(--brand-blue);
    border-radius: 4px;
  }
  .brand-name {
    font-weight: 600;
    font-size: 44px;
    line-height: 1;
    color: var(--brand-blue);
    letter-spacing: -0.5px;
  }
  .person {
    position: absolute;
    left: 40px;
    top: 170px;
    display: flex;
    align-items: baseline;
    gap: 6px;
  }
  .person-name {
    font-weight: 700;
    font-size: 20px;
    color: var(--ink);
  }
  .person-bolt { width: 8px; height: 12px; }
  .person-role {
    font-size: 13px;
    letter-spacing: 0.5px;
    color: var(--brand-blue);
    text-transform: uppercase;
  }
  .contact {
    position: absolute;
    left: 40px;
    top: 214px;
    list-style: none;
    font-size: 16px;
    color: var(--ink);
  }
  .contact li {
    display: flex;
    align-items: center;
    gap: 12px;
    height: 26px;
  }
  .contact svg { width: 14px; height: 14px; flex: none; }
</style>
</head>
<body>
<main class="sheet">

  <section class="card card--back" aria-label="Card back">
    <span class="back-name">Norvale</span>
  </section>

  <section class="card card--front" aria-label="Card front">
    <span class="watermark" aria-hidden="true">Norvale</span>

    <div class="registration">
      <p>ABN 123456789</p>
      <p>Licence # 123456789</p>
    </div>

    <div class="brand">
      <span class="brand-square" aria-hidden="true"></span>
      <span class="brand-name">Norvale Installations</span>
    </div>

    <div class="person">
      <span class="person-name">Mark Daniels</span>
      <svg class="person-bolt" viewBox="0 0 8 12" aria-hidden="true">
        <path d="M5 0 L1 7 H4 L3 12 L7 5 H4 Z" fill="var(--brand-blue)"/>
      </svg>
      <span class="person-role">Electrician</span>
    </div>

    <ul class="contact">
      <li>
        <svg viewBox="0 0 14 14" aria-hidden="true">
          <rect x="3" y="1" width="8" height="12" rx="1.5" fill="none" stroke="var(--brand-blue)" stroke-width="1.6"/>
          <rect x="5.5" y="10.3" width="3" height="1.2" fill="var(--brand-blue)"/>
        </svg>
        <span>+45 2014 8830</span>
      </li>
      <li>
        <svg viewBox="0 0 14 14" aria-hidden="true">
          <circle cx="7" cy="7" r="6" fill="var(--brand-blue)"/>
          <ellipse cx="7" cy="7" rx="2.6" ry="6" fill="none" stroke="#fff" stroke-width="1"/>
          <line x1="1" y1="7" x2="13" y2="7" stroke="#fff" stroke-width="1"/>
        </svg>
        <span>www.norvaleinstall.com.au</span>
      </li>
    </ul>
  </section>

</main>
</body>
</html>
```